Brightwater Counseling Business Card Design Project

I am starting a new business that provides counseling and coaching services to individuals and couples. These individuals are people looking to "transform" or grow in the personal lives. The design should convey trust, intimacy, hope, growth. It should be professional, elegant.
Contact information
Name: Dana K. Whitfield
Title: Counselor and Life Coach
Slogan: Bringing Hope. Transforming Lives.
address: 48310 Route 19, Suite 400
Plymouth, MN 55987
Phone: 763-555-0148
Email: dana@brightwater-cc.example
website: www.brightwater-cc.example
Back side of card should have bullets:
Individual counseling
Relationship counseling
Life Coaching for Teens and Adults
Group Workshops

```html
<!DOCTYPE html>
<html lang="en">
<head>
<meta charset="utf-8">
<title>Brightwater Counseling – Business Card</title>
<link rel="stylesheet" href="https://fonts.googleapis.com/css2?family=PT+Sans:ital,wght@0,400;0,700;1,400&display=swap">
<style>
  :root {
    --backdrop: #e9e7e3;
    --card: #ffffff;
    --ink: #2b2b2b;
    --muted: #555555;
    --brand-blue: #1f5f95;
    --brand-navy: #1d3f66;
    --tab-gray: #5a5a5a;
    --shadow: rgba(0, 0, 0, 0.28);
  }
  * { box-sizing: border-box; margin: 0; padding: 0; }
  html, body { width: 1200px; height: 475px; overflow: hidden; }
  body {
    background: var(--backdrop);
    font-family: "PT Sans", "Myriad Pro", Arial, sans-serif;
    color: var(--ink);
    position: relative;
  }
  .card {
    position: absolute;
    top: 90px;
    width: 524px;
    height: 298px;
    background: var(--card);
    box-shadow: 0 3px 8px var(--shadow);
  }
  .card--front { left: 40px; }
  .card--back { left: 627px; }

  .brand {
    position: absolute;
    display: flex;
    align-items: center;
    gap: 12px;
  }
  .brand__mark {
    width: 46px; height: 46px;
    border-radius: 50%;
    background: var(--brand-blue);
    flex: none;
  }
  .brand__name {
    font-size: 25px;
    font-weight: 400;
    letter-spacing: 1.5px;
    text-transform: uppercase;
    color: var(--brand-navy);
    white-space: nowrap;
  }
  .card--front .brand { left: 22px; top: 38px; }
  .card--back .brand { left: 50%; top: 36px; transform: translateX(-50%); }

  .slogan {
    position: absolute;
    left: 80px; top: 96px;
    font-size: 14px;
    font-style: italic;
    letter-spacing: 0.6px;
    color: var(--brand-blue);
  }

  .edge-tab {
    position: absolute;
    width: 11px;
  }
  .edge-tab--left {
    left: 0; top: 164px; height: 117px;
    background: var(--brand-blue);
    border-radius: 0 6px 6px 0;
  }
  .edge-tab--right {
    right: 0; top: 168px; height: 46px;
    background: var(--tab-gray);
    border-radius: 6px 0 0 6px;
  }

  .contact {
    position: absolute;
    left: 20px; top: 173px;
    font-size: 15px;
    line-height: 19px;
  }
  .contact__line { display: flex; align-items: center; gap: 5px; }
  .contact__line svg { width: 11px; height: 11px; flex: none; }
  .address {
    position: absolute;
    left: 20px; top: 236px;
    font-size: 13px;
    line-height: 19px;
    font-style: normal;
  }
  .holder {
    position: absolute;
    right: 24px; top: 171px;
    text-align: right;
  }
  .holder__name {
    font-size: 17px;
    font-weight: 700;
    color: var(--brand-navy);
  }
  .holder__title {
    font-size: 13px;
    color: var(--muted);
    margin-top: 2px;
  }

  .services {
    position: absolute;
    left: 0; right: 0; top: 112px;
    list-style: none;
    text-align: center;
    font-size: 14px;
    line-height: 22px;
    color: var(--ink);
  }
  .services li::before {
    content: "";
    display: inline-block;
    width: 6px; height: 6px;
    border-radius: 50%;
    background: var(--brand-blue);
    margin-right: 8px;
    vertical-align: middle;
    position: relative;
    top: -1px;
  }
  .website {
    position: absolute;
    left: 0; right: 0; top: 241px;
    text-align: center;
    font-size: 15px;
    letter-spacing: 1.2px;
    color: var(--ink);
  }
</style>
</head>
<body>
  <section class="card card--front" aria-label="Card front">
    <div class="brand">
      <span class="brand__mark"></span>
      <span class="brand__name">Brightwater Counseling</span>
    </div>
    <p class="slogan">Bringing Hope. Transforming Lives.</p>
    <span class="edge-tab edge-tab--left"></span>
    <span class="edge-tab edge-tab--right"></span>

    <div class="contact">
      <p class="contact__line">
        <svg viewBox="0 0 12 12" aria-hidden="true"><circle cx="6" cy="6" r="5.3" fill="none" stroke="#1f5f95" stroke-width="1.2"/><path d="M4 3.2c-.6.5-.6 1.6.3 2.9s2 2 2.8 1.9l.8-.8-1.1-.9-.6.5c-.5-.2-1.1-.9-1.3-1.4l.5-.6-.8-1.1z" fill="#1f5f95"/></svg>
        763-555-0148
      </p>
      <p class="contact__line">
        <svg viewBox="0 0 12 12" aria-hidden="true"><rect x="1" y="3" width="10" height="7" rx="1" fill="#1f5f95"/><path d="M1.5 3.5 6 7l4.5-3.5" fill="none" stroke="#fff" stroke-width="1"/></svg>
        dana@brightwater-cc.example
      </p>
      <p class="contact__line">
        <svg viewBox="0 0 12 12" aria-hidden="true"><circle cx="6" cy="6" r="5" fill="none" stroke="#1f5f95" stroke-width="1.1"/><ellipse cx="6" cy="6" rx="2.2" ry="5" fill="none" stroke="#1f5f95" stroke-width="1"/><path d="M1 6h10" stroke="#1f5f95" stroke-width="1"/></svg>
        www.brightwater-cc.example
      </p>
    </div>
    <address class="address">
      48310 Route 19<br>
      Suite 400, Plymouth, MN 55987
    </address>
    <div class="holder">
      <p class="holder__name">Dana K. Whitfield</p>
      <p class="holder__title">Counselor and Life Coach</p>
    </div>
  </section>

  <section class="card card--back" aria-label="Card back">
    <div class="brand">
      <span class="brand__mark"></span>
      <span class="brand__name">Brightwater Counseling</span>
    </div>
    <ul class="services">
      <li>Individual counseling</li>
      <li>Relationship counseling</li>
      <li>Life Coaching for Teens and Adults</li>
      <li>Group Workshops</li>
    </ul>
    <p class="website">www.brightwater-cc.example</p>
  </section>
</body>
</html>
```